Real Estate Sign

My company is in need of a redesign for our real estate lawn sign. The sign should show our logo, the phrase "For Sale", our phone number 314-587-2049 and website www.HomvexTX.com.
Updates

Hello

Thank you for your submissions.  I am looking for the website and phone number to be very visible from a good distance.  I do also want to stay within the colors of my logo. Too many colors could be expensive to reproduce.

Thank you
Trevor

I favor clean, straight lines and design.  I prefer not to add any other graphics or logos on the sign.  The logo and name are enough. I am looking for readability from a good distance and prefer calls to action like call 314-592-2049 for information or visit www.HomvexTX.com to schedule tour today!  I don't really need FOR SALE to be so prominent.

thanks for all the submissions.
Trevor

Trevor

Industry/Entity Type

Real Estate

```html
<!DOCTYPE html>
<html lang="en">
<head>
<meta charset="utf-8">
<title>Homvex Realty – For Sale Sign</title>
<link rel="stylesheet" href="https://fonts.googleapis.com/css2?family=Open+Sans:wght@300;400;600&display=swap">
<style>
  :root {
    --sky: #00b2ff;
    --navy-mid: #0a4a7c;
    --navy-glow: #1670b8;
    --navy-deep: #04386a;
    --white: #ffffff;
    --page: #ffffff;
  }
  * { margin: 0; padding: 0; box-sizing: border-box; }
  html, body {
    width: 1200px; height: 900px; overflow: hidden;
    background: var(--page);
    font-family: "Open Sans", Arial, sans-serif;
  }
  .sign {
    position: absolute; left: 63px; top: 53px;
    width: 1070px; height: 792px;
    box-shadow: 0 2px 8px rgba(0,0,0,0.35);
    overflow: hidden;
  }
  .status-band {
    height: 123px; background: var(--sky);
    display: flex; align-items: center; justify-content: center;
  }
  .status-band h1 {
    color: var(--white); font-weight: 600; font-size: 80px;
    letter-spacing: 5px; line-height: 1;
  }
  .brand-panel {
    height: 394px;
    background: radial-gradient(ellipse 55% 60% at 50% 50%, var(--navy-glow) 0%, var(--navy-mid) 100%);
    display: flex; align-items: center; justify-content: center;
  }
  .brand-name {
    color: var(--white); font-weight: 400; font-size: 104px;
    letter-spacing: 2px; line-height: 1;
  }
  .contact-panel {
    height: 275px; background: var(--navy-deep);
    color: var(--white); text-align: center;
    position: relative;
  }
  .contact-prompt {
    position: absolute; left: 185px; width: 698px; top: 18px;
    font-weight: 300; font-size: 37px; letter-spacing: 1px;
    padding-bottom: 4px;
    border-bottom: 2px solid var(--white);
    line-height: 1.3;
  }
  .contact-phone {
    position: absolute; left: 0; right: 0; top: 80px;
    font-weight: 400; font-size: 96px; letter-spacing: 3px; line-height: 1;
  }
  .contact-web {
    position: absolute; left: 0; right: 0; top: 178px;
    font-weight: 400; font-size: 62px; letter-spacing: 3px; line-height: 1;
  }
</style>
</head>
<body>
  <div class="sign">
    <header class="status-band"><h1>FOR SALE</h1></header>
    <section class="brand-panel">
      <div class="brand-name">Homvex Realty</div>
    </section>
    <section class="contact-panel">
      <p class="contact-prompt">Please contact us for more information</p>
      <p class="contact-phone">314-592-2049</p>
      <p class="contact-web">www.HomvexTX.com</p>
    </section>
  </div>
</body>
</html>
```